Business Card Design Project

We need a logo design for a new company based in Southern California called "Norvale Security Services, Inc." We install security and camera systems for homeowners and business, to protect their assets.
Updates

Project Deadline Extended
Reason: LOGO Design completes in eight days. Would like that design decided before we finish the business cards. Thanks...

Target Market(s)

Homeowners and business owners looking for additional protection of their assets.

Industry/Entity Type

Security

Font styles to use
Serif

Requirements
Must have
• Company Name
Office# 909-472-3615
Service# 909-472-3616
email: NorvaleSecurity@brimwell.net
address: 48620 Thorncrest Lane Rancho Cucamonga, CA 91704
Nice to have
• Serving Southern California

```html
<!DOCTYPE html>
<html lang="en">
<head>
<meta charset="utf-8">
<title>Norvale Security Services, Inc. — Business Card</title>
<link rel="stylesheet" href="https://fonts.googleapis.com/css2?family=EB+Garamond:wght@400&display=swap">
<style>
  :root {
    --canvas-bg: #e4e6ea;
    --card-top: #07071f;
    --card-violet: #3a2f86;
    --card-blue: #2a5cc0;
    --card-sky: #0a9de2;
    --text-light: #ffffff;
    --text-red: #d9262b;
    --mark-red: #d9262b;
  }
  * { margin: 0; padding: 0; box-sizing: border-box; }
  html, body {
    width: 1021px;
    height: 1200px;
    overflow: hidden;
  }
  body {
    background: var(--canvas-bg);
    display: flex;
    align-items: center;
    justify-content: center;
    font-family: "EB Garamond", Georgia, serif;
  }
  .business-card {
    position: relative;
    width: 600px;
    height: 960px;
    background: linear-gradient(180deg,
      var(--card-top) 0%,
      var(--card-violet) 30%,
      var(--card-blue) 55%,
      var(--card-sky) 100%);
    box-shadow: 0 10px 30px rgba(0,0,0,0.25);
    text-align: center;
  }
  .brand-lockup {
    position: absolute;
    top: 190px;
    left: 0;
    right: 0;
    display: flex;
    align-items: center;
    justify-content: center;
    gap: 18px;
  }
  .brand-dot {
    width: 34px;
    height: 34px;
    border-radius: 50%;
    background: var(--mark-red);
  }
  .brand-name {
    color: var(--text-light);
    font-size: 64px;
    font-weight: 400;
    letter-spacing: 1px;
  }
  .company-name {
    position: absolute;
    top: 460px;
    left: 0;
    right: 0;
    color: var(--text-red);
    font-size: 44px;
    font-weight: 400;
    line-height: 1.45;
  }
  .contact {
    position: absolute;
    left: 0;
    right: 0;
    color: var(--text-light);
    font-size: 32px;
    line-height: 1.38;
  }
  .contact-phones { top: 620px; padding-left: 40px; }
  .contact-address { top: 730px; }
  .contact-email { top: 835px; padding-left: 60px; font-size: 30px; }
  .service-area {
    position: absolute;
    top: 882px;
    left: 0;
    right: 0;
    padding-left: 40px;
    color: var(--text-red);
    font-size: 30px;
  }
</style>
</head>
<body>
  <main class="business-card">
    <div class="brand-lockup">
      <span class="brand-dot"></span>
      <span class="brand-name">Norvale</span>
    </div>
    <h1 class="company-name">Norvale<br>Security Services Inc.</h1>
    <p class="contact contact-phones">Office (909)-472-3615<br>Service (909)-472-3616</p>
    <p class="contact contact-address">48620 Thorncrest Lane<br>Rancho Cucamonga, CA 91704</p>
    <p class="contact contact-email">NorvaleSecurity@brimwell.net</p>
    <p class="service-area">Serving Southern California</p>
  </main>
</body>
</html>
```